Kovalen Spinal Care and Performance

We need new business cards, something more modern, clean. On the back of the card maybe a quote. The Dr. likes, “The doctor of the future will give no medicine, but will interest his patient in the care of the human frame, in diet and in the cause and prevention of disease.” - Walter Brisby. We are open to other suggestions. We are a chiropractic office.

```html
<!DOCTYPE html>
<html lang="en">
<head>
<meta charset="utf-8">
<title>Kovalen Spinal Care and Performance – Business Cards</title>
<link rel="stylesheet" href="https://fonts.googleapis.com/css2?family=Open+Sans:ital,wght@0,400;0,600;0,700;1,400&display=swap">
<style>
  :root {
    --backdrop: #2a2a2c;
    --card: #ffffff;
    --purple: #5e1f6b;
    --green: #8dbb2a;
    --ink: #222222;
    --muted: #3a3a3a;
  }
  * { box-sizing: border-box; margin: 0; padding: 0; }
  html, body {
    width: 1200px; height: 1021px; overflow: hidden;
    background: var(--backdrop);
    font-family: "Open Sans", Arial, sans-serif;
  }
  .stage {
    width: 1200px; height: 1021px;
    display: flex; flex-direction: column; align-items: center; justify-content: center;
    gap: 40px;
  }
  .card {
    width: 800px; height: 457px;
    background: var(--card);
    box-shadow: 0 10px 30px rgba(0,0,0,.5);
    position: relative;
  }
  /* wordmark */
  .wordmark {
    display: flex; align-items: center; gap: 14px;
    color: var(--purple); font-weight: 600;
  }
  .wordmark-dot {
    width: 18px; height: 18px; border-radius: 50%; background: var(--green); flex: none;
  }
  .wordmark-name { font-size: 52px; line-height: 1; letter-spacing: 1px; }
  .wordmark-line { font-size: 15px; letter-spacing: 1.5px; text-transform: uppercase; margin-top: 6px; }

  /* back */
  .card-back {
    display: flex; flex-direction: column; align-items: center; justify-content: center;
    gap: 34px; padding: 0 70px;
  }
  .quote {
    font-style: italic; font-size: 19px; line-height: 1.35; color: var(--ink); text-align: center;
  }
  .quote-author {
    display: block; font-style: normal; color: var(--purple); margin-top: 2px;
  }

  /* front */
  .card-front { display: flex; align-items: center; padding: 0 50px 0 56px; }
  .front-brand { width: 330px; }
  .front-brand .wordmark-name { font-size: 46px; }
  .front-brand .wordmark-line { font-size: 13px; }
  .divider {
    width: 2px; height: 270px; margin: 0 36px 0 34px;
    background: linear-gradient(to bottom, var(--green) 0 28%, #fff 28% 31%, var(--purple) 31% 100%);
  }
  .contact { color: var(--ink); font-size: 20px; line-height: 1.32; }
  .contact-name { color: var(--purple); font-weight: 700; font-size: 25px; }
  .contact-title { font-size: 20px; margin-bottom: 18px; }
  .contact-row { display: flex; align-items: center; gap: 8px; }
  .contact-row svg { width: 18px; height: 18px; flex: none; }
</style>
</head>
<body>
<main class="stage">

  <section class="card card-back" aria-label="Card back">
    <div class="wordmark">
      <span class="wordmark-dot"></span>
      <div>
        <div class="wordmark-name">KOVALEN</div>
        <div class="wordmark-line">Spinal Care &amp; Performance</div>
      </div>
    </div>
    <p class="quote">The Dr. likes, “The doctor of the future will give no medicine, but will interest his patient in the care of the human frame, in diet and in the cause and prevention of disease.”
      <span class="quote-author">- Walter Brisby</span></p>
  </section>

  <section class="card card-front" aria-label="Card front">
    <div class="front-brand wordmark">
      <span class="wordmark-dot"></span>
      <div>
        <div class="wordmark-name">KOVALEN</div>
        <div class="wordmark-line">Spinal Care &amp; Performance</div>
      </div>
    </div>
    <div class="divider"></div>
    <div class="contact">
      <div class="contact-name">Dr. Daniel R. Kovalen</div>
      <div class="contact-title">President</div>
      <div>412 W Maple Ridge Rd, Suite B</div>
      <div>Lakeview, Illinois 60190</div>
      <div class="contact-row">
        <svg viewBox="0 0 24 24" aria-hidden="true"><path fill="var(--green)" d="M6.6 10.8a15 15 0 0 0 6.6 6.6l2.2-2.2a1 1 0 0 1 1-.25 11.4 11.4 0 0 0 3.6.57 1 1 0 0 1 1 1V20a1 1 0 0 1-1 1A17 17 0 0 1 3 4a1 1 0 0 1 1-1h3.5a1 1 0 0 1 1 1c0 1.25.2 2.45.57 3.57a1 1 0 0 1-.25 1z"/></svg>
        <span>(555) 014-2286</span>
      </div>
      <div class="contact-row">
        <svg viewBox="0 0 24 24" aria-hidden="true"><rect x="2.5" y="5" width="19" height="14" fill="none" stroke="var(--green)" stroke-width="2"/><path d="M2.5 5l9.5 8 9.5-8" fill="none" stroke="var(--green)" stroke-width="2"/></svg>
        <span>daniel.k@kovalenspinalcare.com</span>
      </div>
      <div class="contact-row">
        <svg viewBox="0 0 24 24" aria-hidden="true"><g fill="none" stroke="var(--green)" stroke-width="1.8"><circle cx="12" cy="12" r="9.5"/><ellipse cx="12" cy="12" rx="4.2" ry="9.5"/><path d="M2.5 12h19M4 7h16M4 17h16"/></g></svg>
        <span>www.kovalenspinalcare.com</span>
      </div>
    </div>
  </section>

</main>
</body>
</html>
```